Project: Stationary for product web site
Stationary for product web site - Automotive
Bright & Fun-filled
Dorian Feltz
Directory of Marketing
7213 W. Pellam Avenue # 208 Lauderhill, FL, 33329
dorian.feltz@quillmarkgear.com
Xpert Xpert

```html
<!DOCTYPE html>
<html lang="en">
<head>
<meta charset="utf-8">
<title>Quillmark Gear – Business Card</title>
<link href="https://fonts.googleapis.com/css2?family=Montserrat:wght@400;600;800&display=swap" rel="stylesheet">
<style>
  :root {
    --bg: #e9e9ea;
    --blue: #2b3f9e;
    --blue-dark: #1d2a78;
    --blue-light: #4a5fc4;
    --orange: #e8541d;
    --ink: #1b1b1f;
    --text: #4a4d57;
    --white: #ffffff;
    --rule: #c9ccd6;
  }
  * { box-sizing: border-box; margin: 0; padding: 0; }
  html, body { width: 1200px; height: 961px; overflow: hidden; }
  body {
    background: var(--bg);
    font-family: "Montserrat", sans-serif;
    display: flex;
    flex-direction: column;
    align-items: center;
    justify-content: center;
    gap: 50px;
  }
  .card {
    width: 720px;
    height: 411px;
    border-radius: 28px;
    position: relative;
    overflow: hidden;
    box-shadow: 0 6px 22px rgba(0,0,0,0.12);
  }
  .card-back {
    background: linear-gradient(135deg, var(--blue-light) 0%, var(--blue) 50%, var(--blue-dark) 100%);
    display: flex;
    align-items: center;
    justify-content: center;
  }
  .card-back .brand-name {
    font-weight: 800;
    font-size: 54px;
    letter-spacing: 4px;
    color: var(--blue-dark);
    opacity: 0.75;
  }
  .card-front { background: var(--white); }
  .swoosh { position: absolute; inset: 0; width: 720px; height: 411px; }
  .brand {
    position: absolute;
    left: 44px;
    top: 170px;
    width: 230px;
  }
  .brand-name {
    font-weight: 800;
    font-size: 30px;
    letter-spacing: 1px;
    color: var(--blue);
  }
  .brand-tag {
    margin-top: 6px;
    font-size: 10px;
    font-weight: 600;
    letter-spacing: 2.2px;
    text-transform: uppercase;
    color: var(--orange);
  }
  .divider {
    position: absolute;
    left: 292px;
    top: 110px;
    width: 1px;
    height: 200px;
    background: var(--rule);
  }
  .contact {
    position: absolute;
    left: 314px;
    top: 112px;
    width: 300px;
  }
  .person-name {
    font-weight: 800;
    font-size: 22px;
    color: var(--blue);
  }
  .person-title {
    font-size: 12px;
    font-weight: 600;
    color: var(--text);
    margin-top: 2px;
    margin-bottom: 22px;
  }
  .contact-list { list-style: none; }
  .contact-item {
    display: flex;
    align-items: flex-start;
    gap: 10px;
    font-size: 11px;
    line-height: 1.45;
    color: var(--text);
    margin-bottom: 10px;
  }
  .contact-icon { flex: 0 0 14px; width: 14px; height: 14px; margin-top: 1px; }
</style>
</head>
<body>

  <div class="card card-back">
    <span class="brand-name">QUILLMARK</span>
  </div>

  <div class="card card-front">
    <svg class="swoosh" viewBox="0 0 720 411" aria-hidden="true">
      <path d="M470 0 C590 20 690 100 720 190 L720 0 Z" fill="var(--blue)"/>
      <path d="M540 0 C630 18 700 80 720 140 L720 0 Z" fill="var(--orange)"/>
      <path d="M556 0 C640 20 703 75 720 124 L720 0 Z" fill="var(--white)"/>
      <path d="M566 0 C646 20 706 72 720 114 L720 0 Z" fill="var(--ink)"/>
      <path d="M720 316 C703 365 676 395 646 411 L720 411 Z" fill="var(--orange)"/>
      <path d="M720 332 C706 372 686 396 662 411 L720 411 Z" fill="var(--blue)"/>
    </svg>

    <div class="brand">
      <div class="brand-name">QUILLMARK</div>
      <div class="brand-tag">Automotive Parts Supply</div>
    </div>

    <div class="divider"></div>

    <div class="contact">
      <div class="person-name">Dorian Feltz</div>
      <div class="person-title">Directory of Marketing</div>
      <ul class="contact-list">
        <li class="contact-item">
          <svg class="contact-icon" viewBox="0 0 14 14"><path d="M7 1a4 4 0 0 0-4 4c0 3 4 8 4 8s4-5 4-8a4 4 0 0 0-4-4zm0 5.5A1.5 1.5 0 1 1 7 3.5a1.5 1.5 0 0 1 0 3z" fill="var(--blue)"/></svg>
          <span>7213 W. Pellam Avenue # 208<br>Harwick, OR, 97329</span>
        </li>
        <li class="contact-item">
          <svg class="contact-icon" viewBox="0 0 14 14"><rect x="1" y="3" width="12" height="8" rx="1" fill="var(--blue)"/><path d="M1.5 3.5 7 8l5.5-4.5" stroke="#fff" stroke-width="1" fill="none"/></svg>
          <span>dorian.feltz@quillmarkgear.com</span>
        </li>
        <li class="contact-item">
          <svg class="contact-icon" viewBox="0 0 14 14"><circle cx="7" cy="7" r="5.5" fill="none" stroke="var(--blue)" stroke-width="1.4"/><path d="M1.5 7h11M7 1.5c-2 2-2 9 0 11M7 1.5c2 2 2 9 0 11" stroke="var(--blue)" stroke-width="1" fill="none"/></svg>
          <span>www.quillmarkgear.com</span>
        </li>
      </ul>
    </div>
  </div>

</body>
</html>
```